Flyer Design for an electrical and security company trying to build local customers

I need a flyer design for a new company based in Brighton Cove, Sydney 2094 called "Harbor Quill Dune Electrical and Security" also "HQD Electrical and Security". We are electrical contractors who are looking for more local work including emergency service calls and any project work including renovations or new constructions in the local area. I would like everyone in the area to know I am new and that I am available 24 hours a day 7 days a week. I would like to see designs that use the logo colours. Would also like the font of the entire design to be "juice bold".

Electrical

• juice bold

Requirements
Must have
• Must use the colours of the original logo and also have the information from the rear of the card. Must also have services buttons like the website picture attached.

```html
<!DOCTYPE html>
<html lang="en">
<head>
<meta charset="utf-8">
<title>Harbor Quill Dune Electrical and Security – Flyer</title>
<link rel="stylesheet" href="https://fonts.googleapis.com/css2?family=Exo+2:wght@600;700&display=swap">
<style>
  :root {
    --backdrop: #e4e4e4;
    --teal: #5fb4c3;
    --teal-light: #86ccd6;
    --teal-deep: #4a9fb0;
    --orange: #f0874a;
    --orange-light: #f6a56f;
    --orange-deep: #e0733a;
    --charcoal: #4b4b4d;
    --ink: #1c2630;
    --sky: #5ec6ea;
    --paper: #ffffff;
  }
  * { box-sizing: border-box; margin: 0; padding: 0; }
  html, body {
    width: 1200px; height: 900px; overflow: hidden;
    background: var(--backdrop);
    font-family: "Exo 2", "Trebuchet MS", sans-serif;
    font-weight: 700;
  }
  .flyer {
    position: absolute; top: 250px;
    width: 570px; height: 400px;
    overflow: hidden;
    box-shadow: 0 10px 24px rgba(0,0,0,0.22);
  }
  .flyer--front { left: 20px; }
  .flyer--back { left: 610px; }
  .flyer__bg { position: absolute; inset: 0; }

  .brand {
    position: absolute; left: 18px; top: 176px; width: 110px;
    display: flex; align-items: flex-start; gap: 6px;
  }
  .brand__dot {
    flex: none; width: 10px; height: 10px; margin-top: 3px;
    border-radius: 50%; background: var(--teal);
  }
  .brand__name {
    font-size: 12px; line-height: 1.15; font-weight: 700;
    color: var(--charcoal);
  }

  .services { position: absolute; inset: 0; list-style: none; }
  .service {
    position: absolute;
    display: flex; align-items: center; gap: 10px;
    font-size: 17px; line-height: 1; color: var(--ink);
    white-space: nowrap;
  }
  .service__tick { width: 24px; height: 24px; flex: none; }
  .service__text--stack { white-space: normal; line-height: 1.05; }

  .contact {
    position: absolute; right: 16px; top: 200px;
    text-align: right; font-size: 13px; line-height: 1.35;
  }
  .contact--orange { color: var(--orange); }
  .contact--sky { color: var(--sky); }
  .contact__row { display: flex; align-items: center; justify-content: flex-end; gap: 6px; }
  .contact__icon { width: 20px; height: 20px; flex: none; }
</style>
</head>
<body>

<svg width="0" height="0" style="position:absolute" aria-hidden="true">
  <defs>
    <symbol id="tick-teal" viewBox="0 0 26 26">
      <circle cx="13" cy="13" r="13" fill="#ffffff"/>
      <path d="M7.5 13.5 L11.5 17.5 L18.5 8.5" fill="none" stroke="#5fb4c3" stroke-width="3.2" stroke-linecap="round" stroke-linejoin="round"/>
    </symbol>
    <symbol id="tick-orange" viewBox="0 0 26 26">
      <circle cx="13" cy="13" r="13" fill="#ffffff"/>
      <path d="M7.5 13.5 L11.5 17.5 L18.5 8.5" fill="none" stroke="#f0874a" stroke-width="3.2" stroke-linecap="round" stroke-linejoin="round"/>
    </symbol>
    <symbol id="phone" viewBox="0 0 22 22">
      <path d="M7.2 5.5c.5 0 .9.3 1 .8l.6 2.1c.1.4 0 .8-.3 1.1l-.9.8c.7 1.5 1.9 2.7 3.4 3.4l.8-.9c.3-.3.7-.4 1.1-.3l2.1.6c.5.1.8.5.8 1v1.6c0 .6-.5 1.1-1.1 1.1C9.7 17.2 4.8 12.3 4.8 7.3c0-.6.5-1.1 1.1-1.1z" fill="#ffffff"/>
    </symbol>
  </defs>
</svg>

<section class="flyer flyer--front">
  <svg class="flyer__bg" viewBox="0 0 570 400" preserveAspectRatio="none">
    <defs>
      <linearGradient id="teal-facets" x1="0" y1="0" x2="1" y2="1">
        <stop offset="0" stop-color="#86ccd6"/>
        <stop offset="0.5" stop-color="#5fb4c3"/>
        <stop offset="1" stop-color="#4a9fb0"/>
      </linearGradient>
    </defs>
    <rect width="570" height="400" fill="url(#teal-facets)" role="img" aria-label="Low-poly faceted teal background pattern"/>
    <polygon points="0,0 190,0 90,400 0,400" fill="#ffffff"/>
    <polygon points="198,0 206,0 106,400 98,400" fill="#5fb4c3"/>
    <polygon points="500,0 570,0 570,400 400,400" fill="#4b4b4d"/>
    <polygon points="488,0 494,0 394,400 388,400" fill="#4b4b4d"/>
  </svg>

  <div class="brand">
    <span class="brand__dot"></span>
    <span class="brand__name">Harbor Quill Dune Electrical and Security</span>
  </div>

  <ul class="services">
    <li class="service" style="left:204px; top:28px;">
      <svg class="service__tick"><use href="#tick-teal"/></svg>
      <span class="service__text service__text--stack">24 hour<br>emergency service</span>
    </li>
    <li class="service" style="left:195px; top:72px;"><svg class="service__tick"><use href="#tick-teal"/></svg><span class="service__text">new installations</span></li>
    <li class="service" style="left:186px; top:106px;"><svg class="service__tick"><use href="#tick-teal"/></svg><span class="service__text">repairs</span></li>
    <li class="service" style="left:177px; top:140px;"><svg class="service__tick"><use href="#tick-teal"/></svg><span class="service__text">maintenance</span></li>
    <li class="service" style="left:168px; top:174px;"><svg class="service__tick"><use href="#tick-teal"/></svg><span class="service__text">renovations/extensions</span></li>
    <li class="service" style="left:159px; top:208px;"><svg class="service__tick"><use href="#tick-teal"/></svg><span class="service__text">re-writing</span></li>
    <li class="service" style="left:150px; top:242px;"><svg class="service__tick"><use href="#tick-teal"/></svg><span class="service__text">home theatre</span></li>
    <li class="service" style="left:141px; top:276px;"><svg class="service__tick"><use href="#tick-teal"/></svg><span class="service__text">surround sound</span></li>
    <li class="service" style="left:128px; top:320px;"><svg class="service__tick"><use href="#tick-teal"/></svg><span class="service__text">wall tv`s</span></li>
  </ul>

  <div class="contact contact--orange">
    <p>call us today</p>
    <p class="contact__row">
      <svg class="contact__icon" viewBox="0 0 22 22"><circle cx="11" cy="11" r="11" fill="#f0874a"/><use href="#phone"/></svg>
      <span>1300 555 019</span>
    </p>
    <p>Brighton Cove,<br>Sydney 2094</p>
  </div>
</section>

<section class="flyer flyer--back">
  <svg class="flyer__bg" viewBox="0 0 570 400" preserveAspectRatio="none">
    <defs>
      <linearGradient id="orange-facets" x1="0" y1="0" x2="1" y2="1">
        <stop offset="0" stop-color="#f6a56f"/>
        <stop offset="0.5" stop-color="#f0874a"/>
        <stop offset="1" stop-color="#e0733a"/>
      </linearGradient>
    </defs>
    <rect width="570" height="400" fill="url(#orange-facets)" role="img" aria-label="Low-poly faceted orange background pattern"/>
    <polygon points="0,0 22,0 0,88" fill="#ffffff"/>
    <polygon points="30,0 36,0 0,144 0,120" fill="#ffffff" opacity="0.8"/>
    <polygon points="500,0 570,0 570,400 400,400" fill="#4b4b4d"/>
    <polygon points="488,0 494,0 394,400 388,400" fill="#4b4b4d"/>
  </svg>

  <ul class="services">
    <li class="service" style="left:150px; top:110px;"><svg class="service__tick"><use href="#tick-orange"/></svg><span class="service__text">ceiling fans</span></li>
    <li class="service" style="left:141px; top:150px;"><svg class="service__tick"><use href="#tick-orange"/></svg><span class="service__text">testing and tagging</span></li>
    <li class="service" style="left:132px; top:190px;"><svg class="service__tick"><use href="#tick-orange"/></svg><span class="service__text">data</span></li>
    <li class="service" style="left:123px; top:240px;"><svg class="service__tick"><use href="#tick-orange"/></svg><span class="service__text">telephone</span></li>
    <li class="service" style="left:112px; top:290px;"><svg class="service__tick"><use href="#tick-orange"/></svg><span class="service__text">security system</span></li>
  </ul>

  <div class="contact contact--sky">
    <p>call us today</p>
    <p class="contact__row">
      <svg class="contact__icon" viewBox="0 0 22 22"><circle cx="11" cy="11" r="11" fill="#5ec6ea"/><use href="#phone"/></svg>
      <span>1300 555 019</span>
    </p>
    <p>Brighton Cove,<br>Sydney 2094</p>
  </div>
</section>

</body>
</html>
```